STEM business card project for a STEM teacher

I need a business card that is colourful, alive and different to describe my enthusiasm and passion for STEM (Science, Technology, Engineering and Mathematics) teaching
I would like to use specific graphics on the rear of the card. An example of the is can be seen here

https://www.pixelmarsh.example.au/find?q=stem+logo&safe=strict&ref=QX7PLM_enAU481AU481&hl=en-GB&mode=insv&src=menu&tab=img&sa=X&id=0bhVMtR4-EJpwLqXBmYcNdsFgKoRtZwaQ_BVCTHkA&w=1024&h=653#pic=KTMVp552rQ7s_WN:

https://www.pixelmarsh.example.au/find?q=stem+logo&safe=strict&ref=QX7PLM_enAU481AU481&hl=en-GB&mode=insv&src=menu&tab=img&sa=X&id=0bhVMtR4-EJpwLqXBmYcNdsFgKoRtZwaQ_BVCTHkA&w=1024&h=653#pic=UB9ttwKmqeDvaX:

https://www.pixelmarsh.example.au/find?q=stem+logo&safe=strict&ref=QX7PLM_enAU481AU481&hl=en-GB&mode=insv&src=menu&tab=img&sa=X&id=0bhVMtR4-EJpwLqXBmYcNdsFgKoRtZwaQ_BVCTHkA&w=1024&h=653#pic=dwjbXa3ok8r7z-Q:

Industry/Entity Type

Business

Contact Information for Business Card

Owen Brackley
STEM Teacher
Larchmoor College
0455 918 306

Requirements
Must have
• Something that reflects the exciting and changing nature of STEM education
• Eduction is about enabling students to see what they can do and to let them achieve their full potential
• I m absolutely passionate about letting kids enjoy themselves and see how they can use STEM to positively change their world

```html
<!DOCTYPE html>
<html lang="en">
<head>
<meta charset="utf-8">
<title>STEM Teacher Business Card</title>
<link href="https://fonts.googleapis.com/css2?family=Share+Tech+Mono&display=swap" rel="stylesheet">
<style>
  :root {
    --blue: #29a8e0;
    --yellow: #f7b416;
    --orange: #f26b2a;
    --red: #e63950;
    --ink: #5a6b7a;
    --paper: #ffffff;
    --backdrop: #e4e6e9;
  }
  * { margin: 0; padding: 0; box-sizing: border-box; }
  html, body {
    width: 982px; height: 1200px; overflow: hidden;
    background: var(--backdrop);
    font-family: "Share Tech Mono", monospace;
  }
  .canvas { position: relative; width: 982px; height: 1200px; }
  .card {
    position: absolute; left: 61px; width: 860px; height: 520px;
    background: var(--paper); overflow: hidden;
    box-shadow: 0 6px 22px rgba(0,0,0,.12);
  }
  .card--front { top: 40px; }
  .card--back { top: 640px; }
  .card svg.shapes { position: absolute; inset: 0; }

  .stem-line { position: absolute; white-space: nowrap; letter-spacing: .12em; }
  .stem-line .science { color: var(--blue); }
  .stem-line .technology { color: var(--yellow); }
  .stem-line .engineering { color: var(--orange); }
  .stem-line .mathematics { color: var(--red); }
  .stem-line .sep { color: var(--ink); }
  .stem-line--small { left: 40px; top: 272px; font-size: 13px; }
  .stem-line--large { left: 0; right: 0; top: 190px; text-align: center; font-size: 27px; }

  .name {
    position: absolute; left: 530px; top: 124px;
    font-size: 50px; color: var(--paper); letter-spacing: .1em;
  }
  .position {
    position: absolute; right: 60px; top: 200px;
    font-size: 28px; color: var(--blue); letter-spacing: .08em;
  }
  .contact {
    position: absolute; left: 520px; top: 268px;
    list-style: none; font-size: 20px; color: var(--ink);
    line-height: 38px; letter-spacing: .06em;
  }
  .website {
    position: absolute; right: 44px; bottom: 34px;
    font-size: 20px; color: var(--paper); letter-spacing: .1em;
  }
</style>
</head>
<body>
<div class="canvas">

  <section class="card card--front">
    <svg class="shapes" width="860" height="520" viewBox="0 0 860 520">
      <!-- contact stripes -->
      <polygon points="0,112 420,112 400,152 0,152" fill="var(--red)"/>
      <polygon points="0,158 398,158 378,198 0,198" fill="var(--orange)"/>
      <polygon points="0,204 376,204 356,244 0,244" fill="var(--yellow)"/>
      <!-- stripe icons -->
      <g fill="none" stroke="#fff" stroke-width="2">
        <rect x="368" y="120" width="14" height="24" rx="2"/>
        <line x1="372" y1="139" x2="378" y2="139"/>
        <circle cx="353" cy="178" r="11"/>
        <rect x="346" y="173" width="14" height="10"/>
        <polyline points="346,173 353,179 360,173"/>
        <path d="M331 236 c-8 -10 -8 -12 -8 -15 a8 8 0 0 1 16 0 c0 3 0 5 -8 15z"/>
        <circle cx="331" cy="221" r="3"/>
      </g>
      <!-- name ribbon -->
      <polygon points="470,112 860,112 860,192 470,192 500,152" fill="var(--blue)"/>
      <!-- subject icons -->
      <g fill="none" stroke-width="2.2">
        <path d="M600 438 h10 M602 438 v14 l-9 18 h24 l-9 -18 v-14" stroke="var(--blue)"/>
        <g stroke="var(--yellow)">
          <circle cx="672" cy="455" r="13"/><circle cx="672" cy="455" r="5"/>
        </g>
        <g stroke="var(--orange)">
          <rect x="730" y="442" width="26" height="18"/>
          <line x1="724" y1="466" x2="762" y2="466"/>
        </g>
        <g stroke="var(--red)">
          <rect x="794" y="440" width="24" height="30"/>
          <line x1="794" y1="450" x2="818" y2="450"/>
          <line x1="806" y1="450" x2="806" y2="470"/>
          <line x1="794" y1="460" x2="818" y2="460"/>
        </g>
      </g>
    </svg>
    <p class="stem-line stem-line--small">
      <span class="science">SCIENCE</span> <span class="sep">\</span>
      <span class="technology">TECHNOLOGY</span> <span class="sep">\</span>
      <span class="engineering">ENGINEERING</span> <span class="sep">\</span>
      <span class="mathematics">MATHEMATICS</span>
    </p>
    <h1 class="name">YOUR NAME</h1>
    <p class="position">/position/</p>
    <ul class="contact">
      <li>0800 555 800</li>
      <li>youremail@mailbox.example</li>
      <li>Street no 1, City</li>
    </ul>
  </section>

  <section class="card card--back">
    <svg class="shapes" width="860" height="520" viewBox="0 0 860 520">
      <polygon points="0,420 130,420 110,520 0,520" fill="var(--blue)"/>
      <polygon points="130,420 250,420 230,520 110,520" fill="var(--yellow)"/>
      <polygon points="250,420 370,420 350,520 230,520" fill="var(--orange)"/>
      <polygon points="370,420 490,420 470,520 350,520" fill="var(--red)"/>
      <polygon points="490,460 860,460 860,520 470,520" fill="var(--blue)"/>
      <g fill="none" stroke="#fff" stroke-width="2.4">
        <path d="M50 446 h14 M53 446 v16 l-11 20 h30 l-11 -20 v-16"/>
        <circle cx="170" cy="468" r="16"/><circle cx="170" cy="468" r="6"/>
        <rect x="273" y="454" width="32" height="22"/>
        <line x1="266" y1="482" x2="312" y2="482"/>
        <rect x="400" y="450" width="30" height="36"/>
        <line x1="400" y1="462" x2="430" y2="462"/>
        <line x1="415" y1="462" x2="415" y2="486"/>
        <line x1="400" y1="474" x2="430" y2="474"/>
      </g>
    </svg>
    <p class="stem-line stem-line--large">
      <span class="science">SCIENCE</span> <span class="sep">\</span>
      <span class="technology">TECHNOLOGY</span> <span class="sep">\</span>
      <span class="engineering">ENGINEERING</span> <span class="sep">\</span>
      <span class="mathematics">MATHEMATICS</span>
    </p>
    <p class="website">www.yourwebsite.example</p>
  </section>

</div>
</body>
</html>
```